KTV Business Card

Create a Simple but Elegant business card for a Luxury Off Road Vehicle and Accessories sales Company. Center of Letters we usually fill with red or a carbon fiber we don't want to limit creativity so anything goes. I think we would prefer large logo on the front and a smaller logo with infused QR reader on the back.
Some Ideas to get you heading more in the right direction are to put them on a thicker cardstock with red edges and we would need our logo letter (KTV) filled in with red. Example is the Vantorelli card in our brief. For the side with our info on it we are looking for our logo to include an embedded QR reader also in our brief.
Information to include 2 bullet points: Luxury Off Road Vehicle Sales / Custom Off Road Bumpers
Address:518 Pelling Road, Suite 164, Harlan Creek, Nevada
Phone# 555-318-0467,
Website: WWW.KTV-TRAILGEAR.EXAMPLE
Facebook: facebook.com/KTVTrailGear
Instagram: instagram.com/ktv_trailgear
Target Market(s)
Exotic Vehicle and Outdoor enthusiasts.
Industry/Entity Type
Business
Look and feel

```html
<!DOCTYPE html>
<html lang="en">
<head>
<meta charset="utf-8">
<title>KTV Business Card</title>
<link rel="stylesheet" href="https://fonts.googleapis.com/css2?family=Jura:wght@400;500;600;700&family=Michroma&display=swap">
<style>
  :root {
    --stage: #e7e4df;
    --card-white: #fbfbfa;
    --card-dark: #1d1d1f;
    --card-dark-edge: #2c2c2f;
    --ink: #1b1b1b;
    --ink-soft: #3a3a3a;
    --ink-muted: #9a9a9a;
    --light-text: #e4e4e4;
    --badge-fill: #ededed;
  }
  * { box-sizing: border-box; margin: 0; padding: 0; }
  html, body {
    width: 1200px; height: 795px; overflow: hidden;
    background: var(--stage);
  }
  .canvas {
    position: relative; width: 1200px; height: 795px;
    display: flex; align-items: center; justify-content: center; gap: 40px;
  }
  .card {
    position: relative; width: 540px; height: 309px;
    box-shadow: 0 6px 18px rgba(0,0,0,.22);
    font-family: "Jura", sans-serif;
    overflow: hidden;
  }

  /* Front: contact side */
  .card-front { background: var(--card-white); color: var(--ink); }
  .brand { position: absolute; left: 34px; top: 54px; }
  .brand-row { display: flex; align-items: center; gap: 12px; }
  .brand-name {
    font-family: "Jura", sans-serif; font-weight: 700;
    font-size: 52px; line-height: 1; letter-spacing: 4px; color: var(--ink);
  }
  .brand-dot {
    width: 38px; height: 38px; border-radius: 50%; background: var(--ink);
  }
  .brand-tagline {
    margin-top: 6px; font-weight: 700; font-size: 11px;
    letter-spacing: 1.6px; text-transform: uppercase; color: var(--ink);
  }
  .person { position: absolute; left: 330px; top: 96px; }
  .person-name {
    font-family: "Michroma", sans-serif; font-size: 13px;
    letter-spacing: 2.5px; color: var(--ink); white-space: nowrap;
  }
  .person-role {
    margin-top: 6px; font-family: "Michroma", sans-serif; font-size: 9px;
    letter-spacing: 1.8px; color: var(--ink-muted); text-transform: uppercase;
  }
  .contact {
    position: absolute; left: 34px; top: 158px;
    list-style: none; font-size: 11.5px; font-weight: 500; color: var(--ink-soft);
    line-height: 17px;
  }
  .contact li { display: flex; align-items: center; gap: 7px; white-space: nowrap; }
  .contact .icon { width: 10px; height: 10px; flex: none; }
  .icon-square { width: 9px; height: 9px; background: var(--ink-soft); border-radius: 1.5px; flex: none; }

  /* Back: dark side */
  .card-back { background: var(--card-dark); color: var(--light-text); }
  .carbon-texture {
    position: absolute; inset: 0;
    background: radial-gradient(ellipse at 60% 45%, var(--card-dark-edge) 0%, var(--card-dark) 70%);
  }
  .services {
    position: absolute; left: 44px; top: 128px;
    list-style: none; font-size: 15px; font-weight: 500; line-height: 22px;
    letter-spacing: .3px; color: var(--light-text); white-space: nowrap;
  }
  .back-mark {
    position: absolute; left: 300px; top: 96px;
    display: flex; align-items: center; gap: 12px;
  }
  .back-mark .brand-dot { width: 52px; height: 52px; background: var(--badge-fill); }
  .back-mark .brand-name { color: var(--badge-fill); font-size: 56px; }
</style>
</head>
<body>
<main class="canvas">

  <section class="card card-front" aria-label="Card front with contact details">
    <div class="brand">
      <div class="brand-row">
        <span class="brand-name">KTV</span>
        <span class="brand-dot" aria-hidden="true"></span>
      </div>
      <p class="brand-tagline">Custom Off-Road Products</p>
    </div>

    <div class="person">
      <p class="person-name">ALEX MORROW</p>
      <p class="person-role">Director</p>
    </div>

    <ul class="contact">
      <li>518 Pelling Road</li>
      <li>Suite 164</li>
      <li>Harlan Creek, Nevada</li>
      <li>
        <svg class="icon" viewBox="0 0 10 10" aria-hidden="true">
          <path d="M2.2 .8 L3.8 .8 L4.4 3 L3.3 3.8 C3.9 5.2 4.8 6.1 6.2 6.7 L7 5.6 L9.2 6.2 L9.2 7.8 C9.2 8.6 8.6 9.2 7.8 9.2 C4 9 1 6 .8 2.2 C.8 1.4 1.4 .8 2.2 .8 Z" fill="#3a3a3a"/>
        </svg>
        555-318-0467
      </li>
      <li><span class="icon-square" aria-hidden="true"></span>facebook.com/KTVTrailGear</li>
      <li><span class="icon-square" aria-hidden="true"></span>instagram.com/ktv_trailgear</li>
      <li>
        <svg class="icon" viewBox="0 0 10 10" aria-hidden="true">
          <circle cx="5" cy="5" r="4.3" fill="none" stroke="#3a3a3a" stroke-width="1"/>
          <ellipse cx="5" cy="5" rx="1.9" ry="4.3" fill="none" stroke="#3a3a3a" stroke-width=".8"/>
          <line x1=".7" y1="5" x2="9.3" y2="5" stroke="#3a3a3a" stroke-width=".8"/>
        </svg>
        WWW.KTV-TRAILGEAR.EXAMPLE
      </li>
    </ul>
  </section>

  <section class="card card-back" aria-label="Card back with services">
    <div class="carbon-texture" role="img" aria-label="Dark carbon fibre texture background"></div>
    <ul class="services">
      <li>Luxury offroad vehicle sales</li>
      <li>Custom Off Road Bumpers</li>
    </ul>
    <div class="back-mark">
      <span class="brand-dot" aria-hidden="true"></span>
      <span class="brand-name">KTV</span>
    </div>
  </section>

</main>
</body>
</html>
```